Postcard Design for BQAV-

We need a postcard designed that is similar to our current example with information but has a few changes for the season. It needs to be an oversized postcard that meets KRTL BQAV requirements.

In the section that says complete car care, I'd like to add a blurb that Summer is here! Make sure your Car is ready and your:
AC is cold
Cooling system is functioning properly
Tires and Alighment are vacation ready

Elsewhere on the card, we need to add that we offer a 3 year/36,000 warranty on parts and labor

We also need to add that we have a 5.0 Zorvia Review Score and a 4.9 Pavo Nimbal score

Colors can change as can font as long as it is easy to read

```html
<!DOCTYPE html>
<html lang="en">
<head>
<meta charset="utf-8">
<title>Five Anvil Repair – Summer Postcard</title>
<link rel="stylesheet" href="https://fonts.googleapis.com/css2?family=Krona+One&family=Barlow+Semi+Condensed:wght@500;600;700&family=DM+Sans:wght@400;500;700&display=swap">
<style>
  :root {
    --stage: #9b9b9b;
    --paper: #ffffff;
    --ink: #111111;
    --yellow: #f9bd16;
    --gold-text: #d9a12a;
    --edge-grey: #bdbdbf;
    --map-green: #dcebdd;
  }
  * { box-sizing: border-box; margin: 0; padding: 0; }
  html, body { width: 1200px; height: 474px; overflow: hidden; background: var(--stage); }
  body { position: relative; font-family: "DM Sans", sans-serif; color: var(--ink); }

  .card { position: absolute; top: 43px; width: 530px; height: 389px; background: var(--paper); overflow: hidden; }
  .card--front { left: 53px; }
  .card--back { left: 617px; }
  .card > * { position: absolute; }

  .backdrop { left: 0; top: 0; width: 530px; height: 389px; }

  /* shared bands */
  .call-band { left: 0; top: 287px; width: 360px; height: 41px; background: var(--yellow);
    clip-path: polygon(0 0, 100% 0, 92% 100%, 0 100%); display: flex; align-items: center; padding-left: 27px; }
  .call-band__label { font-family: "Barlow Semi Condensed", sans-serif; font-weight: 700; font-size: 15px; margin-right: 9px; }
  .call-band__icon { width: 25px; height: 25px; margin-right: 7px; }
  .call-band__number { font-family: "Krona One", sans-serif; font-size: 24px; letter-spacing: 0.5px; }

  .foot-band { left: 0; top: 334px; height: 55px; background: var(--ink); color: var(--paper);
    display: flex; align-items: center; padding-left: 27px; }
  .foot-band__icon { width: 19px; height: 19px; margin-right: 9px; flex: none; }

  /* front */
  .brand { left: 26px; top: 30px; width: 180px; text-align: center; font-family: "Barlow Semi Condensed", sans-serif;
    font-weight: 700; line-height: 1.02; font-size: 24px; letter-spacing: 1px; }
  .brand__small { display: block; font-size: 13px; letter-spacing: 2px; }

  .warranty { left: 340px; top: 28px; width: 190px; }
  .warranty__intro { position: absolute; left: 20px; top: 0; width: 170px; text-align: center;
    font-family: "Barlow Semi Condensed", sans-serif; font-weight: 700; font-size: 17px; line-height: 1; }
  .warranty__term { position: absolute; left: 15px; top: 20px; width: 175px; height: 23px; background: var(--ink); color: var(--yellow);
    clip-path: polygon(8% 0, 100% 0, 100% 100%, 0 100%); font-family: "Barlow Semi Condensed", sans-serif; font-weight: 700;
    font-size: 20px; line-height: 23px; padding-left: 27px; }
  .warranty__word { position: absolute; left: 0; top: 45px; width: 190px; height: 26px; background: var(--yellow);
    clip-path: polygon(8% 0, 100% 0, 100% 100%, 0 100%); font-family: "Barlow Semi Condensed", sans-serif; font-weight: 700;
    font-size: 27px; line-height: 27px; padding-left: 42px; }
  .warranty__note { position: absolute; left: 20px; top: 77px; width: 170px; text-align: center; font-weight: 500; font-size: 12.5px; }

  .tab { left: 0; height: 32px; background: var(--yellow); clip-path: polygon(0 0, 100% 0, 88% 100%, 0 100%);
    font-family: "Krona One", sans-serif; font-size: 19px; line-height: 33px; padding-left: 26px; }
  .tab--quality { top: 142px; width: 236px; }
  .headline { left: 24px; top: 183px; font-family: "Krona One", sans-serif; font-size: 38px; line-height: 1; letter-spacing: -0.5px; }
  .subline { left: 27px; top: 226px; display: flex; align-items: center; font-family: "Barlow Semi Condensed", sans-serif;
    font-weight: 700; font-size: 22px; }
  .subline__amp { width: 18px; height: 18px; border-radius: 50%; background: var(--yellow); font-size: 12px; line-height: 18px;
    text-align: center; margin-right: 8px; }
  .perk { left: 27px; top: 253px; color: var(--gold-text); font-weight: 500; font-size: 13.5px; }
  .foot-band--front { width: 300px; clip-path: polygon(0 0, 100% 0, 88% 100%, 0 100%); }
  .address { font-weight: 500; font-size: 12.5px; line-height: 1.25; }

  /* back */
  .tab--complete { top: 32px; width: 208px; height: 33px; font-size: 18px; }
  .car-care { left: 25px; top: 74px; font-family: "Krona One", sans-serif; font-size: 31px; line-height: 1; }
  .car-care__note { left: 25px; top: 106px; color: var(--gold-text); font-weight: 500; font-size: 13px; }

  .sender { left: 299px; top: 26px; display: flex; font-size: 8.6px; line-height: 1.25; }
  .sender__pin { width: 13px; height: 13px; margin-right: 9px; flex: none; }
  .sender__address { width: 96px; }
  .permit { left: 422px; top: 28px; font-size: 8.6px; line-height: 1.25; border-left: 1px solid var(--yellow); padding-left: 15px; height: 40px; }
  .mail-band { left: 286px; top: 78px; width: 244px; height: 35px; background: var(--yellow);
    clip-path: polygon(10% 0, 100% 0, 100% 100%, 0 100%); font-size: 8.6px; line-height: 1.2; padding: 7px 0 0 34px; }

  .rating { top: 132px; display: flex; flex-direction: column; align-items: center; white-space: nowrap; }
  .rating--zorvia { left: 328px; width: 84px; }
  .rating--pavo { left: 420px; width: 106px; }
  .rating__name { font-weight: 700; font-size: 16px; line-height: 1.2; }
  .rating__score { font-size: 12px; line-height: 1.2; color: var(--gold-text); margin-top: 4px; }
  .rating__score .stars { color: var(--yellow); letter-spacing: 0.5px; }

  .season { left: 26px; top: 136px; font-family: "Barlow Semi Condensed", sans-serif; font-weight: 700; font-size: 30px;
    line-height: 1; padding-bottom: 4px; border-bottom: 2px solid var(--yellow); width: 200px; white-space: nowrap; }
  .checklist-intro { left: 26px; top: 182px; font-family: "Barlow Semi Condensed", sans-serif; font-weight: 500; font-size: 12.5px; }
  .checklist { left: 26px; top: 202px; list-style: none; }
  .checklist li { display: flex; align-items: center; height: 19.5px; font-family: "Barlow Semi Condensed", sans-serif;
    font-weight: 500; font-size: 14px; }
  .checklist svg { width: 15px; height: 13px; margin-right: 9px; }
  .foot-band--back { width: 318px; clip-path: polygon(0 0, 100% 0, 90% 100%, 0 100%); }
  .website { font-weight: 500; font-size: 15px; }
</style>
</head>
<body>

<section class="card card--front">
  <svg class="backdrop" viewBox="0 0 530 389" role="img" aria-label="Photo of a mechanic's hands working in a car engine bay">
    <defs>
      <linearGradient id="engine-tone" x1="0" y1="0" x2="1" y2="1">
        <stop offset="0" stop-color="#4a4a4e"/>
        <stop offset="0.5" stop-color="#8a7f78"/>
        <stop offset="1" stop-color="#1e1e20"/>
      </linearGradient>
    </defs>
    <path d="M240 389 L430 160 Q448 138 480 136 L530 136 L530 389 Z" fill="var(--edge-grey)"/>
    <path d="M262 389 L446 170 Q462 150 492 147 L530 147 L530 389 Z" fill="url(#engine-tone)"/>
  </svg>

  <div class="brand">FIVE ANVIL<span class="brand__small">AUTOMOTIVE</span>REPAIR</div>

  <div class="warranty">
    <div class="warranty__intro">WE INCLUDE</div>
    <div class="warranty__term">3 YEAR/36,000</div>
    <div class="warranty__word">WARRANTY</div>
    <div class="warranty__note">on parts and labor</div>
  </div>

  <div class="tab tab--quality">HIGH QUALITY</div>
  <h1 class="headline">AUTO REPAIR</h1>
  <div class="subline"><span class="subline__amp">&amp;</span>PREVENTIVE MAINTENANCE</div>
  <p class="perk">Complimentary pick up, drop off, and loaners</p>

  <div class="call-band">
    <span class="call-band__label">CALL US</span>
    <svg class="call-band__icon" viewBox="0 0 24 24"><circle cx="12" cy="12" r="12" fill="var(--ink)"/><path d="M8.3 5.5c.5-.3 1.1-.2 1.4.3l1.2 2c.3.5.2 1-.2 1.4l-.9.8c.6 1.4 1.7 2.6 3.1 3.3l.8-.9c.4-.4 1-.5 1.4-.2l2 1.2c.5.3.6.9.3 1.4l-.8 1.2c-.5.7-1.4 1-2.2.8-3.8-1.1-6.7-4-7.8-7.8-.2-.8.1-1.7.8-2.2z" fill="var(--paper)"/></svg>
    <span class="call-band__number">555.014.0287</span>
  </div>

  <div class="foot-band foot-band--front">
    <svg class="foot-band__icon" viewBox="0 0 20 20"><circle cx="10" cy="10" r="10" fill="var(--yellow)"/><path d="M10 4.5a3.6 3.6 0 0 0-3.6 3.6c0 2.7 3.6 6.7 3.6 6.7s3.6-4 3.6-6.7A3.6 3.6 0 0 0 10 4.5zm0 5a1.4 1.4 0 1 1 0-2.8 1.4 1.4 0 0 1 0 2.8z" fill="var(--ink)"/></svg>
    <p class="address">218 Harrowgate Rd Unit B,<br>Maple Hollow, PA 17000</p>
  </div>
</section>

<section class="card card--back">
  <svg class="backdrop" viewBox="0 0 530 389" role="img" aria-label="Street map showing the shop location">
    <path d="M282 389 L430 208 Q448 186 480 185 L530 185 L530 389 Z" fill="var(--edge-grey)"/>
    <path d="M303 389 L445 218 Q460 200 490 193 L530 193 L530 389 Z" fill="var(--map-green)"/>
  </svg>

  <div class="tab tab--complete">COMPLETE</div>
  <h1 class="car-care">CAR CARE</h1>
  <p class="car-care__note">including inspections and emissions</p>

  <div class="sender">
    <svg class="sender__pin" viewBox="0 0 20 20"><circle cx="10" cy="10" r="10" fill="var(--yellow)"/><path d="M10 4.5a3.6 3.6 0 0 0-3.6 3.6c0 2.7 3.6 6.7 3.6 6.7s3.6-4 3.6-6.7A3.6 3.6 0 0 0 10 4.5zm0 5a1.4 1.4 0 1 1 0-2.8 1.4 1.4 0 0 1 0 2.8z" fill="var(--ink)"/></svg>
    <p class="sender__address">Five Anvil Repair<br>218 Harrowgate Rd<br>Unit B, Maple Hollow,<br>PA 17000</p>
  </div>
  <p class="permit">PRSRT STD<br>ECRWSS<br>KRTL POSTAGE<br>PAID BQAV RETAIL</p>
  <div class="mail-band">****************ECRWSS****BQAV<br>Local Postal Customer</div>

  <div class="rating rating--zorvia">
    <span class="rating__name">Zorvia</span>
    <span class="rating__score">5.0 <span class="stars">★★★★★</span></span>
  </div>
  <div class="rating rating--pavo">
    <span class="rating__name">Pavo Nimbal</span>
    <span class="rating__score"><span class="stars">★★★★★</span> 4.9</span>
  </div>

  <h2 class="season">Summer is here!</h2>
  <p class="checklist-intro">MAKE SURE YOUR CAR IS READY AND YOUR:</p>
  <ul class="checklist">
    <li><svg viewBox="0 0 15 13"><path d="M1 7l4 4 9-10" fill="none" stroke="var(--yellow)" stroke-width="3" stroke-linecap="round" stroke-linejoin="round"/></svg>AC is cold</li>
    <li><svg viewBox="0 0 15 13"><path d="M1 7l4 4 9-10" fill="none" stroke="var(--yellow)" stroke-width="3" stroke-linecap="round" stroke-linejoin="round"/></svg>Cooling system is functioning properly</li>
    <li><svg viewBox="0 0 15 13"><path d="M1 7l4 4 9-10" fill="none" stroke="var(--yellow)" stroke-width="3" stroke-linecap="round" stroke-linejoin="round"/></svg>Tires and Alignment are road trip ready</li>
  </ul>

  <div class="call-band">
    <span class="call-band__label">CALL US</span>
    <svg class="call-band__icon" viewBox="0 0 24 24"><circle cx="12" cy="12" r="12" fill="var(--ink)"/><path d="M8.3 5.5c.5-.3 1.1-.2 1.4.3l1.2 2c.3.5.2 1-.2 1.4l-.9.8c.6 1.4 1.7 2.6 3.1 3.3l.8-.9c.4-.4 1-.5 1.4-.2l2 1.2c.5.3.6.9.3 1.4l-.8 1.2c-.5.7-1.4 1-2.2.8-3.8-1.1-6.7-4-7.8-7.8-.2-.8.1-1.7.8-2.2z" fill="var(--paper)"/></svg>
    <span class="call-band__number">555.014.0287</span>
  </div>

  <div class="foot-band foot-band--back">
    <svg class="foot-band__icon" viewBox="0 0 20 20"><circle cx="10" cy="10" r="10" fill="var(--yellow)"/><g fill="none" stroke="var(--ink)" stroke-width="1.2"><circle cx="10" cy="10" r="5.5"/><ellipse cx="10" cy="10" rx="2.4" ry="5.5"/><path d="M4.5 10h11M5.3 7.2h9.4M5.3 12.8h9.4"/></g></svg>
    <p class="website">fiveanvilrepair.com</p>
  </div>
</section>

</body>
</html>
```